Major infrastructure project needs a diagram designed

We need two simple diagrams created on Sydney's current (1) and future (2) intermodal terminal capacity and the number of shipping containers coming out of Kellmere Dock.

Please see attached file for full instructions (Word and PDF attached)

```html
<!DOCTYPE html>
<html lang="en">
<head>
<meta charset="utf-8">
<title>Freight capacity of Sydney's intermodal terminals</title>
<link href="https://fonts.googleapis.com/css2?family=Overpass:wght@400;600;700;800&display=swap" rel="stylesheet">
<style>
  :root {
    --header-dark: #2c3846;
    --header-panel: #3a4858;
    --band-teal: #2394a8;
    --ink: #2e3744;
    --chart-bg: #d3e9ee;
    --imex: #f5b335;
    --imex-line: #e39a1c;
    --interstate: #3e4958;
    --interstate-line: #2b3440;
    --combined: #2690a4;
    --combined-line: #1b6f80;
    --storage: #c9cbcd;
    --storage-line: #a9acaf;
    --rail-grey: #c8cbce;
    --road-grey: #9aa0a7;
    --white: #ffffff;
  }
  * { margin: 0; padding: 0; box-sizing: border-box; }
  html, body { width: 1200px; height: 848px; overflow: hidden; background: var(--white); }
  body { font-family: "Overpass", "Helvetica Neue", Arial, sans-serif; color: var(--ink); position: relative; }

  .masthead {
    position: absolute; left: 0; top: 0; width: 1200px; height: 172px;
    background: var(--header-dark);
  }
  .masthead__scene {
    position: absolute; left: 8px; top: 0; width: 1184px; height: 160px;
    background: linear-gradient(90deg, #4a5a6a 0%, #3c4a5a 45%, #34414f 75%, #2f3b48 100%);
  }
  .masthead__title {
    position: absolute; left: 42px; top: 66px;
    font-size: 33px; font-weight: 800; color: var(--white); letter-spacing: 0.3px;
    white-space: pre;
  }
  .section-band {
    position: absolute; left: 0; top: 172px; width: 1200px; height: 45px;
    background: var(--band-teal);
  }
  .section-band__label {
    position: absolute; left: 42px; top: 13px;
    font-size: 17px; font-weight: 800; letter-spacing: 0.6px; color: var(--ink);
  }
  .section-band__label strong { color: var(--white); font-weight: 800; }

  .chart-svg { position: absolute; left: 0; top: 0; width: 1200px; height: 848px; }

  .axis-label, .tick-label, .value, .dock-sub {
    position: absolute; font-size: 12.5px; font-weight: 700; color: var(--ink);
  }
  .axis-label { left: 256px; top: 292px; width: 88px; text-align: right; }
  .tick-label { top: 292px; width: 80px; text-align: center; }

  .terminal { position: absolute; left: 42px; font-size: 18px; color: var(--ink); }
  .value { left: 262px; width: 66px; text-align: right; }

  .dock-name {
    position: absolute; left: 940px; top: 266px; width: 214px; text-align: center;
    font-size: 18px; font-weight: 700;
  }
  .dock-sub { left: 940px; top: 292px; width: 214px; text-align: center; font-size: 12px; }
  .flow { position: absolute; font-size: 12.5px; color: var(--ink); white-space: nowrap; }
  .flow b { font-weight: 700; }
  .flow--rail { left: 960px; top: 327px; }
  .flow--road { left: 926px; top: 465px; width: 214px; text-align: center; }

  .legend {
    position: absolute; left: 42px; top: 663px; width: 1099px; height: 58px;
    border: 1px solid var(--ink);
  }
  .legend__text { position: absolute; font-size: 11.5px; line-height: 13px; color: var(--ink); }
</style>
</head>
<body>

<header class="masthead">
  <div class="masthead__scene" role="img" aria-label="Container cranes silhouetted against a dark slate sky at the port"></div>
  <h1 class="masthead__title">Freight capacity of Sydney's  intermodal terminals</h1>
</header>

<div class="section-band">
  <h2 class="section-band__label"><strong>CURRENT</strong> INTERMODALS CAPACITY</h2>
</div>

<svg class="chart-svg" viewBox="0 0 1200 848" aria-hidden="true">
  <defs>
    <pattern id="stripe-imex" width="4" height="26" patternUnits="userSpaceOnUse">
      <rect width="4" height="26" fill="var(--imex)"/><rect x="3" width="1" height="26" fill="var(--imex-line)"/>
    </pattern>
    <pattern id="stripe-interstate" width="4" height="26" patternUnits="userSpaceOnUse">
      <rect width="4" height="26" fill="var(--interstate)"/><rect x="3" width="1" height="26" fill="var(--interstate-line)"/>
    </pattern>
    <pattern id="stripe-combined" width="4" height="26" patternUnits="userSpaceOnUse">
      <rect width="4" height="26" fill="var(--combined)"/><rect x="3" width="1" height="26" fill="var(--combined-line)"/>
    </pattern>
    <pattern id="stripe-storage" width="4" height="26" patternUnits="userSpaceOnUse">
      <rect width="4" height="26" fill="var(--storage)"/><rect x="3" width="1" height="26" fill="var(--storage-line)"/>
    </pattern>
  </defs>

  <!-- chart field -->
  <rect x="262" y="318" width="596" height="270" fill="var(--chart-bg)"/>
  <line x1="42" y1="317" x2="858" y2="317" stroke="var(--ink)" stroke-width="1.5"/>
  <line x1="42" y1="590" x2="858" y2="590" stroke="var(--ink)" stroke-width="1.5"/>
  <g stroke="var(--ink)" stroke-width="1">
    <line x1="372" y1="309" x2="372" y2="317"/><line x1="396.3" y1="313" x2="396.3" y2="317"/>
    <line x1="420.6" y1="313" x2="420.6" y2="317"/><line x1="444.9" y1="313" x2="444.9" y2="317"/>
    <line x1="469.2" y1="313" x2="469.2" y2="317"/><line x1="493.5" y1="309" x2="493.5" y2="317"/>
    <line x1="517.8" y1="313" x2="517.8" y2="317"/><line x1="542.1" y1="313" x2="542.1" y2="317"/>
    <line x1="566.4" y1="313" x2="566.4" y2="317"/><line x1="590.7" y1="313" x2="590.7" y2="317"/>
    <line x1="615" y1="309" x2="615" y2="317"/><line x1="639.3" y1="313" x2="639.3" y2="317"/>
    <line x1="663.6" y1="313" x2="663.6" y2="317"/><line x1="687.9" y1="313" x2="687.9" y2="317"/>
    <line x1="712.2" y1="313" x2="712.2" y2="317"/><line x1="736.5" y1="309" x2="736.5" y2="317"/>
    <line x1="760.8" y1="313" x2="760.8" y2="317"/><line x1="785.1" y1="313" x2="785.1" y2="317"/>
    <line x1="809.4" y1="313" x2="809.4" y2="317"/><line x1="833.7" y1="313" x2="833.7" y2="317"/>
    <line x1="858" y1="309" x2="858" y2="317"/>
  </g>

  <!-- Yennora 110,000 -->
  <g class="bar bar--combined" fill="url(#stripe-combined)">
    <rect x="373" y="334" width="60" height="26"/><rect x="435" y="334" width="61" height="26"/>
    <rect x="498" y="334" width="61" height="26"/><rect x="561" y="334" width="61" height="26"/>
    <rect x="624" y="334" width="15" height="26"/>
  </g>
  <!-- Villawood 20,000 -->
  <g class="bar bar--imex" fill="url(#stripe-imex)">
    <rect x="373" y="376" width="48" height="26"/>
  </g>
  <!-- Minto 150,000 -->
  <g class="bar bar--imex" fill="url(#stripe-imex)">
    <rect x="373" y="418" width="60" height="26"/><rect x="435" y="418" width="61" height="26"/>
    <rect x="498" y="418" width="61" height="26"/><rect x="561" y="418" width="61" height="26"/>
    <rect x="624" y="418" width="61" height="26"/><rect x="687" y="418" width="50" height="26"/>
  </g>
  <!-- Chullora 200,000 -->
  <g class="bar bar--interstate" fill="url(#stripe-interstate)">
    <rect x="373" y="460" width="60" height="26"/><rect x="435" y="460" width="61" height="26"/>
    <rect x="498" y="460" width="61" height="26"/><rect x="561" y="460" width="61" height="26"/>
    <rect x="624" y="460" width="61" height="26"/><rect x="687" y="460" width="61" height="26"/>
    <rect x="750" y="460" width="61" height="26"/><rect x="813" y="460" width="45" height="26"/>
  </g>
  <!-- Cooks River, St Peters 150,000 -->
  <g class="bar bar--storage" fill="url(#stripe-storage)">
    <rect x="373" y="502" width="60" height="26"/><rect x="435" y="502" width="61" height="26"/>
    <rect x="498" y="502" width="61" height="26"/><rect x="561" y="502" width="61" height="26"/>
    <rect x="624" y="502" width="61" height="26"/><rect x="687" y="502" width="50" height="26"/>
  </g>
  <!-- Enfield 50,000 -->
  <g class="bar bar--imex" fill="url(#stripe-imex)">
    <rect x="373" y="544" width="60" height="26"/><rect x="435" y="544" width="59" height="26"/>
  </g>

  <!-- dock flows -->
  <polygon points="903,335 915,318 1140,318 1140,352 915,352" fill="var(--rail-grey)"/>
  <polyline points="924,320 913,335 924,350" fill="none" stroke="var(--white)" stroke-width="3"/>
  <rect x="924" y="360" width="216" height="229" fill="var(--road-grey)"/>
  <polygon points="903,377 915,360 928,360 916,377 928,394 915,394" fill="var(--road-grey)"/>
  <polygon points="903,473 915,456 928,456 916,473 928,490 915,490" fill="var(--road-grey)"/>
  <polygon points="903,570 915,553 928,553 916,570 928,587 915,587" fill="var(--road-grey)"/>

  <!-- train icon -->
  <g class="icon-train" fill="var(--ink)">
    <rect x="931" y="322" width="18" height="20" rx="5"/>
    <rect x="934" y="326" width="12" height="6" rx="1" fill="var(--rail-grey)"/>
    <circle cx="935" cy="337" r="1.5" fill="var(--rail-grey)"/><circle cx="945" cy="337" r="1.5" fill="var(--rail-grey)"/>
    <line x1="933" y1="342" x2="928" y2="349" stroke="var(--ink)" stroke-width="1.5"/>
    <line x1="947" y1="342" x2="952" y2="349" stroke="var(--ink)" stroke-width="1.5"/>
    <line x1="927" y1="347" x2="953" y2="347" stroke="var(--ink)" stroke-width="1"/>
  </g>
  <!-- truck icon -->
  <g class="icon-truck" fill="var(--ink)">
    <rect x="1022" y="437" width="30" height="17"/>
    <path d="M1006 443 h13 v11 h-16 v-6 z"/>
    <rect x="1008" y="445" width="6" height="4" fill="var(--road-grey)"/>
    <circle cx="1011" cy="456" r="3"/><circle cx="1029" cy="456" r="3"/><circle cx="1045" cy="456" r="3"/>
    <line x1="1003" y1="460" x2="1055" y2="460" stroke="var(--ink)" stroke-width="1"/>
  </g>

  <!-- legend swatches -->
  <rect x="54" y="682" width="60" height="26" fill="url(#stripe-imex)"/>
  <rect x="281" y="682" width="60" height="26" fill="url(#stripe-interstate)"/>
  <rect x="508" y="682" width="60" height="26" fill="url(#stripe-combined)"/>
  <rect x="732" y="682" width="60" height="26" fill="url(#stripe-storage)"/>
</svg>

<div class="axis-label">TEUs/annum</div>
<div class="tick-label" style="left:332px">0</div>
<div class="tick-label" style="left:454px">50,000</div>
<div class="tick-label" style="left:575px">100,000</div>
<div class="tick-label" style="left:697px">150,000</div>
<div class="tick-label" style="left:818px">200,000</div>

<div class="terminal" style="top:336px">Yennora</div>
<div class="terminal" style="top:378px">Villawood</div>
<div class="terminal" style="top:420px">Minto</div>
<div class="terminal" style="top:462px">Chullora</div>
<div class="terminal" style="top:504px">Cooks River, St Peters</div>
<div class="terminal" style="top:546px">Enfield</div>

<div class="value" style="top:341px">110,000</div>
<div class="value" style="top:383px">20,000</div>
<div class="value" style="top:425px">150,000</div>
<div class="value" style="top:467px">200,000</div>
<div class="value" style="top:509px">150,000</div>
<div class="value" style="top:551px">50,000</div>

<div class="dock-name">Kellmere Dock</div>
<div class="dock-sub">2 million TEUs/annum</div>
<div class="flow flow--rail"><b>300,000 by railway</b> (15%)</div>
<div class="flow flow--road"><b>1.7 million by road</b>&nbsp; (85%)</div>

<div class="legend">
  <div class="legend__text" style="left:82px;top:18px">IMEX (import-export)<br>Terminal</div>
  <div class="legend__text" style="left:309px;top:24px">Interstate Terminal</div>
  <div class="legend__text" style="left:537px;top:24px">IMEX &amp; Interstate</div>
  <div class="legend__text" style="left:760px;top:24px">Storage Empty Containers</div>
</div>

</body>
</html>
```